Dental Office Needs Exciting New Stationary

We need a stationary design that incorporates the logo that we already have and would like to keep the existing color scheme. We need something clean and professional. This is a Endodontic (root canals) office and must represent a dental specialist's office. I need a design for a business card, envelope, and letterhead that all coordinate. I would like the business card to incorporate the information in the business card sample that I am providing. I made the business card design myself but would like to see a better one.

```html
<!DOCTYPE html>
<html lang="en">
<head>
<meta charset="utf-8">
<title>Summit Endodontics – Business Card</title>
<link href="https://fonts.googleapis.com/css2?family=Questrial&display=swap" rel="stylesheet">
<style>
  :root{
    --brand-blue:#1d5fae;
    --brand-blue-deep:#123f86;
    --brand-blue-light:#2f86c8;
    --brand-gray:#9a9ea3;
    --card-white:#eef0f1;
    --ink:#3a3d40;
    --page:#e4e6e8;
  }
  *{margin:0;padding:0;box-sizing:border-box;}
  html,body{width:1200px;height:900px;overflow:hidden;background:var(--page);}
  body{font-family:"Questrial",sans-serif;color:var(--ink);position:relative;}

  .card{position:absolute;left:285px;width:630px;height:360px;border-radius:4px;overflow:hidden;box-shadow:0 6px 18px rgba(0,0,0,.18);}
  .card--back{top:60px;background:radial-gradient(ellipse at 60% 40%,var(--brand-blue-light) 0%,var(--brand-blue) 45%,var(--brand-blue-deep) 100%);color:#fff;}
  .card--front{top:480px;background:var(--card-white);}

  .brand{position:absolute;display:flex;align-items:center;gap:18px;}
  .brand__dot{width:46px;height:46px;border-radius:50%;flex:none;}
  .brand__rule{width:1px;height:74px;flex:none;}
  .brand__name{font-size:30px;letter-spacing:2px;text-transform:uppercase;line-height:1;}

  .card--back .brand{left:120px;top:118px;}
  .card--back .brand__dot{background:#7fb3e0;}
  .card--back .brand__rule{background:rgba(255,255,255,.6);}
  .card--back .brand__name{color:#fff;}
  .card--back .site{position:absolute;left:0;right:0;top:250px;text-align:center;font-size:17px;letter-spacing:1px;}

  .card--front .brand{left:52px;top:40px;}
  .card--front .brand__dot{background:var(--brand-blue);}
  .card--front .brand__rule{background:var(--brand-gray);}
  .card--front .brand__name{color:var(--brand-blue);}

  .doctors{position:absolute;left:52px;top:150px;font-size:17px;white-space:nowrap;}
  .doctors .sep{color:var(--brand-blue);margin:0 6px;}

  .contact{position:absolute;top:186px;font-size:13.5px;line-height:19px;list-style:none;}
  .contact--left{left:58px;}
  .contact--right{left:330px;}
  .contact li{display:flex;align-items:flex-start;gap:9px;}
  .contact svg{width:13px;height:13px;margin-top:3px;flex:none;fill:var(--brand-blue);}

  .swoosh{position:absolute;inset:0;width:630px;height:360px;}
  .card--front .site{position:absolute;right:22px;bottom:16px;color:#fff;font-size:15px;letter-spacing:.5px;}
</style>
</head>
<body>

<section class="card card--back" aria-label="Business card back">
  <div class="brand">
    <span class="brand__dot"></span>
    <span class="brand__rule"></span>
    <span class="brand__name">Summit Endodontics</span>
  </div>
  <p class="site">summitendodontics.com</p>
</section>

<section class="card card--front" aria-label="Business card front">
  <svg class="swoosh" viewBox="0 0 630 360" aria-hidden="true">
    <path d="M230 360 C400 348 545 318 630 236 L630 250 C545 330 400 358 250 360 Z" fill="var(--brand-gray)"/>
    <path d="M262 360 C420 352 555 326 630 258 L630 360 Z" fill="var(--brand-blue)"/>
  </svg>

  <div class="brand">
    <span class="brand__dot"></span>
    <span class="brand__rule"></span>
    <span class="brand__name">Summit Endodontics</span>
  </div>

  <p class="doctors">Daniel R Whitmore DDS MS<span class="sep">•</span>Marco L Bellari DDS</p>

  <ul class="contact contact--left">
    <li><svg viewBox="0 0 16 16"><path d="M3.5 1l3 3-1.7 1.9a9 9 0 0 0 5.3 5.3L12 9.5l3 3-2 2.5C6.5 14.5 1.5 9.5 1 3z"/></svg>555.014.2366</li>
    <li><svg viewBox="0 0 16 16"><path d="M4 1h7l1 2v3H4zM2 7h12v6h-2v2H4v-2H2zM5 11v3h6v-3z"/></svg>555.014.5929</li>
    <li><svg viewBox="0 0 16 16"><path d="M8 0a5.5 5.5 0 0 1 5.5 5.5C13.5 10 8 16 8 16S2.5 10 2.5 5.5A5.5 5.5 0 0 1 8 0zm0 3.3a2.2 2.2 0 1 0 0 4.4 2.2 2.2 0 0 0 0-4.4z"/></svg><span>418 Elm Street<br>Riverton, CA 95010</span></li>
  </ul>

  <ul class="contact contact--right">
    <li><svg viewBox="0 0 16 16"><path d="M3.5 1l3 3-1.7 1.9a9 9 0 0 0 5.3 5.3L12 9.5l3 3-2 2.5C6.5 14.5 1.5 9.5 1 3z"/></svg>555.018.1101</li>
    <li><svg viewBox="0 0 16 16"><path d="M4 1h7l1 2v3H4zM2 7h12v6h-2v2H4v-2H2zM5 11v3h6v-3z"/></svg>555.018.0602</li>
    <li><svg viewBox="0 0 16 16"><path d="M8 0a5.5 5.5 0 0 1 5.5 5.5C13.5 10 8 16 8 16S2.5 10 2.5 5.5A5.5 5.5 0 0 1 8 0zm0 3.3a2.2 2.2 0 1 0 0 4.4 2.2 2.2 0 0 0 0-4.4z"/></svg><span>7200 Harbor Ave. Suite #2<br>Lakeview, CA 95620</span></li>
  </ul>

  <p class="site">summitendodontics.com</p>
</section>

</body>
</html>
```